RV Park - Advertising RV Park using Billboard 12 ft wide by 6 ft tall size

We need a sign for a relatively new RV Park called Bramblewood of Carver RV Park at 2745 Danbury Road, Murphy , NC. The sign should include our web address and phone number. bramblewoodcarverrv.example, 555-314-2967. We would like to see designs that include nice color and no tacky cartoons. Final design should communicate a nice and safe RV Park. We would also like to include quick directions - Just Ahead! Left on Kestrel Rd then left on Danbury Rd. (A nice motor home or RV representation may be nice but not mandatory to be included.) Classic but eye catching design. Sign is 12 ft wide by 6 ft tall in size. Will likely be vinyl printed.

```html
<!DOCTYPE html>
<html lang="en">
<head>
<meta charset="UTF-8">
<title>Bramblewood of Carver RV Park – Billboard</title>
<link href="https://fonts.googleapis.com/css2?family=Black+Ops+One&family=Montserrat:wght@600;700&display=swap" rel="stylesheet">
<style>
  :root {
    --page-bg: #f4efe9;
    --brand-orange: #e0842a;
    --white: #ffffff;
    --ink: #1d1a17;
    --scene-gold: #c98a34;
    --scene-amber: #a9671f;
    --scene-dusk: #6b4a22;
    --scene-light: #f1c46a;
  }
  * { margin: 0; padding: 0; box-sizing: border-box; }
  html, body {
    width: 1199px;
    height: 1200px;
    overflow: hidden;
    background: var(--page-bg);
  }
  .billboard {
    position: absolute;
    left: 90px;
    top: 346px;
    width: 1019px;
    height: 510px;
    background: var(--brand-orange);
    overflow: hidden;
    box-shadow: 0 6px 18px rgba(0,0,0,0.25);
  }
  .campsite-photo {
    position: absolute;
    left: 340px;
    top: 0;
    width: 679px;
    height: 100%;
    background:
      radial-gradient(ellipse at 60% 40%, var(--scene-light) 0%, rgba(241,196,106,0) 45%),
      radial-gradient(ellipse at 55% 90%, var(--scene-dusk) 0%, rgba(107,74,34,0) 60%),
      linear-gradient(180deg, var(--scene-gold) 0%, var(--scene-amber) 60%, var(--scene-dusk) 100%);
  }
  .photo-fade {
    position: absolute;
    left: 340px;
    top: 0;
    width: 340px;
    height: 100%;
    background: linear-gradient(90deg, var(--brand-orange) 0%, rgba(224,132,42,0.75) 45%, rgba(224,132,42,0) 100%);
  }
  .park-name {
    position: absolute;
    left: 47px;
    top: 40px;
    font-family: "Black Ops One", "Impact", sans-serif;
    font-weight: 400;
    font-size: 56px;
    line-height: 62px;
    color: var(--white);
    text-transform: uppercase;
    letter-spacing: 0.5px;
  }
  .directions {
    position: absolute;
    left: 47px;
    top: 236px;
    font-family: "Montserrat", sans-serif;
    font-weight: 700;
    font-size: 17px;
    line-height: 24px;
    color: var(--white);
  }
  .address-band {
    position: absolute;
    left: 0;
    top: 278px;
    width: 640px;
    height: 44px;
    background: linear-gradient(90deg, var(--white) 0%, var(--white) 55%, rgba(255,255,255,0.35) 85%, rgba(255,255,255,0) 100%);
    display: flex;
    align-items: center;
    padding-left: 47px;
  }
  .address {
    font-family: "Montserrat", sans-serif;
    font-weight: 700;
    font-size: 19px;
    color: var(--ink);
  }
  .contact-list {
    position: absolute;
    left: 47px;
    top: 374px;
    list-style: none;
  }
  .contact-item {
    display: flex;
    align-items: center;
    gap: 14px;
    height: 44px;
    font-family: "Montserrat", sans-serif;
    font-weight: 700;
    font-size: 29px;
    color: var(--white);
  }
  .contact-icon { width: 24px; height: 24px; flex: none; }
</style>
</head>
<body>
  <section class="billboard">
    <div class="campsite-photo" role="img" aria-label="Vintage camper trailer with open door and a wooden deck with rocking chairs, set among autumn trees at golden hour"></div>
    <div class="photo-fade"></div>

    <h1 class="park-name">Bramblewood<br>of Carver<br>RV Park</h1>
    <p class="directions">Just Ahead! Left on Kestrel Rd then left on Danbury Rd</p>

    <div class="address-band">
      <p class="address">2745 Danbury Road, Murphy , NC</p>
    </div>

    <ul class="contact-list">
      <li class="contact-item">
        <svg class="contact-icon" viewBox="0 0 24 24" aria-hidden="true">
          <path fill="#ffffff" d="M6.6 3.5c.5-.5 1.3-.5 1.7.1l2 2.7c.4.5.3 1.2-.1 1.6l-1.3 1.2c.9 2 2.5 3.6 4.5 4.5l1.2-1.3c.4-.4 1.1-.5 1.6-.1l2.7 2c.6.4.6 1.2.1 1.7l-1.6 1.6c-.8.8-2 1.1-3.1.7C9.6 16.7 7.3 14.4 5.8 9.7c-.4-1.1-.1-2.3.7-3.1z"/>
          <path fill="none" stroke="#ffffff" stroke-width="1.8" stroke-linecap="round" d="M14 3.5a6.5 6.5 0 0 1 6.5 6.5M14 7a3 3 0 0 1 3 3"/>
        </svg>
        <span>555-314-2967</span>
      </li>
      <li class="contact-item">
        <svg class="contact-icon" viewBox="0 0 24 24" aria-hidden="true">
          <circle cx="12" cy="12" r="10" fill="#ffffff"/>
          <g fill="none" stroke="#e0842a" stroke-width="1.6">
            <ellipse cx="12" cy="12" rx="4" ry="9"/>
            <path d="M3 12h18M5 7.5h14M5 16.5h14"/>
          </g>
        </svg>
        <span>bramblewoodcarverrv.example</span>
      </li>
    </ul>
  </section>
</body>
</html>
```